Tallow Glen Grand Opening Invitation

I need an invitation designed for a grand opening event we are hosting at a new apartment home community.

Industry/Entity Type

Apartment

Requirements
Must have
• Tallow Glen logo; date: Wednesday, October 19 from 5:00 - 7:00; Tallow Glen Apartments Homes invites you to its Grand Opening Celebration; A ribbon cutting ceremony kicks off the festivities as we welcome you to Mishawaka's most unique and contemporary apartment home community.
• Tallow Glen Apartment Homes
• 482 N. Copperfield Ave.
• Mishawaka, IN 46545
• (877) 555-0142
• www.tallowglenhaus.example

```html
<!DOCTYPE html>
<html lang="en">
<head>
<meta charset="utf-8">
<title>Tallow Glen Grand Opening Invitation</title>
<link href="https://fonts.googleapis.com/css2?family=Cinzel:wght@500;600&family=Arvo:ital,wght@1,700&family=Catamaran:wght@500&display=swap" rel="stylesheet">
<style>
  :root {
    --paper: #ffffff;
    --ink-brown: #5c270b;
    --heading-brown: #6a2d0f;
    --copper-dark: #6e3208;
    --copper: #c8733a;
    --copper-mid: #e39a62;
    --copper-light: #f8c898;
    --bullet: #e6a878;
    --steel: #c9cbcf;
  }
  html, body {
    margin: 0;
    padding: 0;
    overflow: hidden;
    background: var(--paper);
  }
  .invitation {
    position: relative;
    width: 1200px;
    height: 899px;
    background: var(--paper);
    overflow: hidden;
    font-family: "Catamaran", "Helvetica Neue", Arial, sans-serif;
    color: var(--ink-brown);
  }
  .ribbon-art {
    position: absolute;
    left: 0;
    top: 30px;
    width: 250px;
    height: 285px;
    background: linear-gradient(135deg, var(--copper-light), var(--copper) 45%, var(--copper-dark));
  }
  .ribbon-cut-art {
    position: absolute;
    left: 762px;
    top: 220px;
    width: 438px;
    height: 100px;
    background: linear-gradient(90deg, var(--steel), var(--copper) 35%, var(--copper-light) 75%, var(--copper));
  }
  .base-band {
    position: absolute;
    left: 0;
    bottom: 0;
    width: 1200px;
    height: 230px;
  }
  .brand {
    position: absolute;
    top: 34px;
    left: 0;
    width: 1200px;
    text-align: center;
  }
  .brand-dot {
    display: block;
    width: 84px;
    height: 84px;
    margin: 0 auto 22px;
    border-radius: 50%;
    background: var(--copper);
  }
  .brand-name {
    font-family: "Cinzel", Georgia, serif;
    font-weight: 600;
    font-size: 40px;
    letter-spacing: 4px;
    color: var(--copper);
    margin: 0;
    line-height: 1;
  }
  .invite-line {
    position: absolute;
    top: 327px;
    left: 0;
    width: 1200px;
    text-align: center;
    margin: 0;
    font-family: "Cinzel", Georgia, serif;
    font-weight: 600;
    font-size: 20px;
    color: var(--heading-brown);
  }
  .title-rule {
    position: absolute;
    left: 278px;
    width: 652px;
    height: 2px;
    background: linear-gradient(90deg, var(--copper-dark), var(--copper-mid) 60%, var(--copper));
  }
  .title-rule.top { top: 374px; }
  .title-rule.bottom { top: 433px; }
  .event-title {
    position: absolute;
    top: 381px;
    left: 0;
    width: 1200px;
    margin: 0;
    text-align: center;
    font-family: "Cinzel", Georgia, serif;
    font-weight: 600;
    font-size: 40px;
    line-height: 48px;
    color: var(--heading-brown);
  }
  .event-date {
    position: absolute;
    top: 456px;
    left: 0;
    width: 1200px;
    margin: 0;
    text-align: center;
    font-family: "Arvo", Georgia, serif;
    font-style: italic;
    font-weight: 700;
    font-size: 23.5px;
    color: var(--ink-brown);
  }
  .contact {
    position: absolute;
    top: 544px;
    left: 172px;
    margin: 0;
    padding: 0;
    list-style: none;
    font-size: 20.5px;
    line-height: 26.5px;
  }
  .contact li {
    position: relative;
    padding-left: 26px;
  }
  .contact li::before {
    content: "";
    position: absolute;
    left: 2px;
    top: 9px;
    width: 9px;
    height: 9px;
    border-radius: 50%;
    background: var(--bullet);
  }
  .divider {
    position: absolute;
    left: 510px;
    top: 523px;
    width: 1.5px;
    height: 174px;
    background: var(--copper);
  }
  .welcome {
    position: absolute;
    top: 563px;
    left: 537px;
    width: 485px;
    margin: 0;
    font-size: 20px;
    line-height: 26px;
  }
</style>
</head>
<body>
<main class="invitation">
  <div class="ribbon-art" role="img" aria-label="Swirling copper satin ribbon"></div>
  <div class="ribbon-cut-art" role="img" aria-label="Silver scissors cutting the copper ribbon"></div>

  <header class="brand">
    <span class="brand-dot"></span>
    <p class="brand-name">Tallow Glen</p>
  </header>

  <p class="invite-line">Tallow Glen Apartments Homes invites you to</p>
  <div class="title-rule top"></div>
  <h1 class="event-title">Grand Opening Celebration</h1>
  <div class="title-rule bottom"></div>
  <p class="event-date">Wednesday, October 19 from 5:00 - 7:00</p>

  <ul class="contact">
    <li>Tallow Glen Apartment Homes<br>482 N. Copperfield Ave.<br>Mishawaka, IN 46545</li>
    <li>(877) 555-0142</li>
    <li>www.tallowglenhaus.example</li>
  </ul>

  <div class="divider"></div>

  <p class="welcome">A ribbon cutting ceremony kicks off the festivities as we welcome you to Mishawaka's most unique &amp; contemporary apartment home community.</p>

  <svg class="base-band" viewBox="0 0 1200 230" preserveAspectRatio="none" aria-hidden="true">
    <defs>
      <linearGradient id="bandCopper" x1="0" y1="0" x2="1" y2="0">
        <stop offset="0" stop-color="#6e3208"/>
        <stop offset="0.4" stop-color="#e39a62"/>
        <stop offset="0.68" stop-color="#f8c898"/>
        <stop offset="1" stop-color="#b9622a"/>
      </linearGradient>
    </defs>
    <path d="M 0 12 C 300 90, 850 110, 1200 10 L 1200 230 L 0 230 Z" fill="url(#bandCopper)"/>
  </svg>
</main>
</body>
</html>
```